bramblegate crest roofing flyer*

I need an a5 size flyer designing to go in our local advertising magazine.We are based in the north west of England Id like key features from the website including on the flyer, possibly even reviews, what we do ect.I don't however want it too busy, simple pictures and description of service.company colours and logo. I require simple one sided business cards toonumber, web address and logowinner will receive a request to design around 5 different double sided a5 flyers too, each with all our services on one side and the other primarily for one service we have provided locally with a spacve to put the house number down.REPAIRSROOFLINEFLAT ROOFS PITCHED ROOFSSYNTHETIC ROOFSUP TO 50 YEARS WARRANTY AVAILABLERANKED THE #1 FLAT ROOFER IN THE UK OUT OF 787 REGISTERED FLAT ROOFING COMPANIESRANKED THE #10 ROOFING COMPANY IN THE UK OUT OF 1976 REGISTERED SPECIALIST ROOFING COMPANIESBOTH FOR COST, CUSTOMER SERVICE AND QUALITY WITH 5 STAR REVIEWSGUARANTEED TO FIND AND FIX A LEAKAPPROVED INSTALLERSAWARD WINNINGTIME SERVED FIXED PRICES

Target Market(s)

homeowners

Colors

Designer to choose only greyscale colors for use in the design.

Requirements
Must have
• contact details
• pictures of my work
• clear and simple

```html
<!DOCTYPE html>
<html lang="en">
<head>
<meta charset="utf-8">
<title>Bramblegate Crest Roofing – Flyer</title>
<link href="https://fonts.googleapis.com/css2?family=Montserrat:wght@400;500;600;700;800&family=Raleway:wght@400;600&display=swap" rel="stylesheet">
<style>
:root{
  --green:#3b8a34;
  --green-deep:#285d27;
  --green-panel:#387530;
  --orange:#f1a918;
  --gold:#d9a72a;
  --white:#ffffff;
  --ink:#1d1d1d;
  --page:#e6e6e6;
}
*{margin:0;padding:0;box-sizing:border-box}
html,body{width:1200px;height:1000px;overflow:hidden;background:var(--page)}
body{font-family:'Montserrat',sans-serif;position:relative}
.flyer{position:absolute;left:268px;top:30px;width:664px;height:940px;background:var(--white);overflow:hidden;box-shadow:0 2px 8px rgba(0,0,0,.12)}
.header{position:absolute;left:0;top:0;width:664px;height:140px}
.brand{position:absolute;left:22px;top:22px;color:var(--green);font-weight:800;font-size:34px;line-height:1.02;letter-spacing:.5px;text-transform:uppercase}
.roof-art{position:absolute;right:0;top:18px;width:320px;height:122px}
.intro{position:absolute;left:0;top:140px;width:664px;height:100px;background:var(--green);color:var(--white);font-size:13.4px;line-height:16px;letter-spacing:.6px;text-align:justify;padding:19px 20px 0 20px;font-family:'Raleway',sans-serif}
.services{position:absolute;left:0;top:240px;width:664px;height:266px;background:var(--green-deep)}
.services-tab{position:absolute;left:0;top:26px;width:178px;height:32px;background:#2f6a2d;clip-path:polygon(0 0,100% 0,96% 100%,0 100%);color:var(--white);font-size:16px;padding:6px 0 0 22px}
.services-tab b{font-weight:700}
.service-list{position:absolute;left:18px;top:72px;list-style:none}
.service-list li{color:var(--white);font-weight:700;font-size:17.5px;height:33.3px;display:flex;align-items:center}
.service-list li::before{content:"";width:7px;height:7px;border-radius:50%;background:var(--white);margin-right:11px}
.claims{position:absolute;left:258px;top:18px;width:406px;height:218px;background:var(--green-panel);border-radius:22px 0 0 22px;clip-path:polygon(10% 0,100% 0,100% 100%,0 100%)}
.claims ul{list-style:none;position:absolute;left:30px;top:22px;width:370px}
.claims li{color:var(--white);font-size:12px;font-weight:500;line-height:15.5px;text-transform:uppercase;position:relative;padding-left:14px;margin-bottom:7px}
.claims li::before{content:"";position:absolute;left:0;top:6px;width:4px;height:4px;border-radius:50%;background:#1d3f1c}
.claims b{font-weight:700}
.claims .big{font-size:14px;font-weight:700}
.claims li:nth-child(2){margin-left:-6px}
.claims li:nth-child(3){margin-left:-14px}
.claims li:nth-child(4){margin-left:-20px}
.claims li:nth-child(5){margin-left:-26px}
.claims li:nth-child(6){margin-left:-30px}
.work{position:absolute;left:0;top:511px;width:664px;height:128px}
.reviews{position:absolute;left:0;top:650px;width:664px;height:162px;background:var(--orange)}
.reviews-tab{position:absolute;left:0;top:28px;width:32px;height:106px;background:var(--white);border-radius:0 10px 10px 0;display:flex;align-items:center;justify-content:center}
.reviews-tab span{transform:rotate(-90deg);color:var(--orange);font-weight:600;font-size:15px;white-space:nowrap}
.review{position:absolute;top:32px;height:104px;border:1.5px solid var(--white);border-radius:10px;color:var(--white)}
.review p{font-family:'Raleway',sans-serif;font-size:11.6px;line-height:16px;text-align:justify;padding:16px 9px 0 9px}
.stars{position:absolute;right:14px;top:-10px;background:var(--orange);padding:0 4px;font-size:17px;letter-spacing:1px;line-height:18px}
.reviewer{position:absolute;left:10px;bottom:-10px;background:var(--orange);padding:0 6px;font-size:15px;font-weight:700;line-height:18px}
.reviewer small{font-weight:400;font-size:11.5px}
.review-one{left:45px;width:300px}
.review-two{left:357px;width:300px}
.contact{position:absolute;left:0;top:812px;width:664px;height:128px}
.call{position:absolute;left:53px;top:20px;font-size:17px;font-weight:500;color:var(--ink)}
.phone{position:absolute;left:51px;top:40px;font-size:31px;font-weight:700;color:var(--ink);letter-spacing:.3px}
.web{position:absolute;left:51px;top:82px;font-size:21.5px;font-weight:500;color:var(--ink);letter-spacing:.4px}
.icon-box{position:absolute;left:0;width:42px;height:32px;background:var(--orange);border-radius:0 6px 6px 0;display:flex;align-items:center;justify-content:center}
.icon-phone{top:46px}
.icon-web{top:81px}
.upto{position:absolute;left:583px;top:14px;font-size:10.5px;font-weight:500;color:var(--ink)}
.badges{position:absolute;left:460px;top:10px;width:200px;height:110px}
</style>
</head>
<body>
<div class="flyer">

  <header class="header">
    <div class="brand">Bramblegate<br>Crest<br>Roofing</div>
    <div class="roof-art" role="img" aria-label="Illustration of green house rooftops with windows"
         style="background:linear-gradient(100deg,rgba(59,138,52,0) 0%,rgba(59,138,52,.85) 35%,var(--green) 100%)"></div>
  </header>

  <section class="intro">
    We're a small family run business with a wealth of roofing experience. We will give a dedicated, personalised approach to all jobs to complete the job with great care and always take our time to do it properly at a fair price. So that the customers will be met with an unrivalled service.
  </section>

  <section class="services">
    <div class="services-tab">OUR <b>SERVICES</b></div>
    <ul class="service-list">
      <li>ROOFING REPAIRS</li>
      <li>ROOFLINE</li>
      <li>FLAT ROOFING</li>
      <li>PITCHED ROOFING</li>
      <li>SYNTHETIC ROOFING</li>
    </ul>
    <div class="claims">
      <ul>
        <li><span class="big">#1</span> <b>In the UK out of 768</b> flat roofing specialists</li>
        <li><span class="big">#10</span> <b>Roofing company in the UK</b> out of 1976 registered specialist roofing companies for <b>cost, customer service &amp; quality</b></li>
        <li><b>Guaranteed to find and fix leaks</b></li>
        <li><b>Fixed fair prices &amp; time served</b></li>
        <li><b>Award winning</b> company</li>
        <li><b>Highly recommended</b> by all customers with <b>5 star reviews</b></li>
      </ul>
    </div>
  </section>

  <svg class="work" viewBox="0 0 664 128" aria-hidden="false">
    <defs>
      <linearGradient id="workOne" x1="0" y1="0" x2="0" y2="1"><stop offset="0" stop-color="#a9c2dc"/><stop offset=".5" stop-color="#b9714e"/><stop offset="1" stop-color="#7d4b33"/></linearGradient>
      <linearGradient id="workTwo" x1="0" y1="0" x2="0" y2="1"><stop offset="0" stop-color="#9a6b4c"/><stop offset=".6" stop-color="#c4c7c9"/><stop offset="1" stop-color="#6b3a2c"/></linearGradient>
      <linearGradient id="workThree" x1="0" y1="0" x2="0" y2="1"><stop offset="0" stop-color="#7b5a63"/><stop offset=".55" stop-color="#a88f68"/><stop offset="1" stop-color="#7a7453"/></linearGradient>
    </defs>
    <path role="img" aria-label="Photo of a finished pitched roof on a red brick house" d="M0 0 H215 Q222 0 220 10 L206 118 Q204 128 194 128 H0 Z" fill="url(#workOne)"/>
    <path role="img" aria-label="Photo of a new flat roof among tiled roofs" d="M236 0 H458 Q466 0 464 10 L452 118 Q450 128 440 128 H222 Q212 128 214 118 L226 10 Q228 0 236 0 Z" fill="url(#workTwo)"/>
    <path role="img" aria-label="Photo of a re-roofed stone outbuilding" d="M478 0 H664 V128 H466 Q456 128 458 118 L470 10 Q472 0 478 0 Z" fill="url(#workThree)"/>
  </svg>

  <section class="reviews">
    <div class="reviews-tab"><span>Reviews</span></div>
    <div class="review review-one">
      <span class="stars">★★★★★</span>
      <p>Excellent job done of re-roofing my extension roof in rubber tiles looks great, the lads were very polite and professional in all aspects of the job would definitely recommend them to anyone. Thanks!</p>
      <span class="reviewer">Tom Haddock <small>- 21 Sep 2019</small></span>
    </div>
    <div class="review review-two">
      <span class="stars">★★★★★</span>
      <p>I rang about my leaking gutter, and they came around the same day. Very courteous and optimistic professional workers. I cannot recommend them enough and definitely would use them again. Thanks!</p>
      <span class="reviewer">Julia Penrose <small>- 12 Jun 2019</small></span>
    </div>
  </section>

  <footer class="contact">
    <div class="call">CALL NOW!</div>
    <div class="icon-box icon-phone">
      <svg width="18" height="18" viewBox="0 0 24 24"><path d="M6.6 10.8a15.1 15.1 0 0 0 6.6 6.6l2.2-2.2a1 1 0 0 1 1-.25 11.4 11.4 0 0 0 3.6.57 1 1 0 0 1 1 1V20a1 1 0 0 1-1 1A17 17 0 0 1 3 4a1 1 0 0 1 1-1h3.5a1 1 0 0 1 1 1c0 1.25.2 2.45.57 3.57a1 1 0 0 1-.25 1z" fill="#1d1d1d"/></svg>
    </div>
    <div class="phone">078 555 013 42</div>
    <div class="icon-box icon-web">
      <svg width="20" height="20" viewBox="0 0 24 24" fill="none" stroke="#1d1d1d" stroke-width="1.8"><circle cx="12" cy="12" r="9"/><path d="M3 12h18M12 3c3 3 3 15 0 18M12 3c-3 3-3 15 0 18"/></svg>
    </div>
    <div class="web">www.bramblegatecrestroofing.com</div>
    <div class="upto">UP TO</div>
    <svg class="badges" viewBox="0 0 200 110">
      <rect x="14" y="6" width="96" height="34" rx="6" fill="#eeeeee"/>
      <circle cx="56" cy="76" r="31" fill="var(--gold)" opacity=".85"/>
      <circle cx="161" cy="60" r="38" fill="#2b2b2b"/>
      <circle cx="161" cy="60" r="31" fill="var(--gold)"/>
    </svg>
  </footer>

</div>
</body>
</html>
```